chiptune chip tuning car tuning company need a banner as advertising

we need a professional banner for outdoor advertising. please as vector.

we are a chip tuning company in germany.

what should be on it:
Chip tuning from € 299

More performance, less consumption

01639840517
www.nedrav.de

CHIPTUNING - Eco-Optimization - AGR / DPF SERVICE - ZÖL certificate - SOFTWARE DEVELOPMENT - File service
-------------------------------------------------- ------------------------------------------
in German:

we need a banner for outdoor advertising. please as vector.

what should be on it:

Chip tuning from € 299

Telephone number: 01639840517
www.nedrav.de

```html
<!DOCTYPE html>
<html lang="de">
<head>
<meta charset="utf-8">
<title>Nedrav Banner – Optionen</title>
<link href="https://fonts.googleapis.com/css2?family=Montserrat:ital,wght@0,500;0,600;0,700;0,800;1,600&display=swap" rel="stylesheet">
<style>
  :root {
    --board: #ffffff;
    --label: #3a3a3c;
    --dark-1: #2e2e30;
    --dark-2: #0c0c0d;
    --gold-1: #b08a3e;
    --gold-2: #ecd393;
    --gold-3: #a27a34;
    --ink: #2f2f31;
    --white: #ffffff;
  }
  html, body {
    margin: 0;
    width: 1200px;
    height: 848px;
    overflow: hidden;
    background: var(--board);
    font-family: "Montserrat", sans-serif;
  }
  .board { position: relative; width: 1200px; height: 848px; }
  .option-label {
    position: absolute;
    left: 163px;
    font-weight: 700;
    font-size: 18px;
    color: var(--label);
    margin: 0;
  }
  .banner {
    position: absolute;
    left: 334px;
    width: 618px;
    height: 353px;
    overflow: hidden;
    background: linear-gradient(90deg, var(--dark-1) 0%, var(--dark-2) 75%);
  }
  .banner p, .banner ul { white-space: nowrap; }
  .banner__photo { position: absolute; inset: 0; }
  .banner__band { position: absolute; inset: 0; }
  .brand {
    position: absolute;
    left: 24px;
    top: 30px;
    font-weight: 800;
    font-size: 44px;
    line-height: 1;
    letter-spacing: 3px;
    color: var(--gold-2);
    margin: 0;
  }
  .price {
    position: absolute;
    left: 20px;
    top: 114px;
    font-weight: 700;
    font-size: 70px;
    letter-spacing: -4px;
    color: var(--ink);
    line-height: 1;
    margin: 0;
  }
  .price__lead {
    position: absolute;
    left: 20px;
    top: 184px;
    font-weight: 700;
    font-size: 20px;
    line-height: 1;
    color: var(--ink);
    margin: 0;
  }
  .tagline {
    position: absolute;
    left: 205px;
    top: 155px;
    font-weight: 600;
    font-style: italic;
    font-size: 11.5px;
    letter-spacing: 2px;
    line-height: 15px;
    color: var(--ink);
    margin: 0;
  }
  .services {
    position: absolute;
    top: 253px;
    list-style: none;
    margin: 0;
    padding: 0;
    font-weight: 500;
    font-size: 8.5px;
    letter-spacing: 1.2px;
    line-height: 10.6px;
    color: var(--white);
  }
  .services--left { left: 15px; }
  .services--right { left: 172px; }
  .contact {
    position: absolute;
    left: 15px;
    top: 303px;
    font-weight: 800;
    font-size: 11.5px;
    line-height: 1;
    letter-spacing: 3.2px;
    color: var(--white);
    margin: 0;
  }
</style>
</head>
<body>
<div class="board">

  <p class="option-label" style="top:275px">OPT.1</p>
  <section class="banner" style="top:53px">
    <svg class="banner__photo" width="618" height="353" role="img" aria-label="Schwarz-weißes Foto eines Motors mit Riemenscheiben und Keilriemen">
      <defs>
        <linearGradient id="engineTone" x1="0" y1="0" x2="1" y2="1">
          <stop offset="0" stop-color="#3a3a3a"/>
          <stop offset="0.45" stop-color="#9a9a9a"/>
          <stop offset="1" stop-color="#1e1e1e"/>
        </linearGradient>
      </defs>
      <polygon points="422,0 618,0 618,353 321,353" fill="url(#engineTone)"/>
    </svg>
    <svg class="banner__band" width="618" height="353" aria-hidden="true">
      <defs>
        <linearGradient id="goldBand1" x1="0" y1="0" x2="1" y2="0">
          <stop offset="0" stop-color="var(--gold-1)"/>
          <stop offset="0.45" stop-color="var(--gold-2)"/>
          <stop offset="1" stop-color="var(--gold-3)"/>
        </linearGradient>
      </defs>
      <polygon points="0,111 408,111 371,226 0,226" fill="url(#goldBand1)"/>
    </svg>
    <p class="brand">NEDRAV</p>
    <p class="price">299€</p>
    <p class="price__lead">CHIPTUNING AB</p>
    <p class="tagline">MEHR LEISTUNG,<br>WENIGER VERBRAUCH</p>
    <ul class="services services--left">
      <li>· CHIPTUNING</li>
      <li>· ECO-OPTIMIERUNG</li>
      <li>· AGR / DPF DEAKTIVIERUNG</li>
    </ul>
    <ul class="services services--right">
      <li>· ZÖL GUTACHTEN</li>
      <li>· SOFTWAREENTWICKLUNG</li>
      <li>· CODIERSERVICE</li>
    </ul>
    <p class="contact">www.nedrav.de | Tel: 01639840517</p>
  </section>

  <p class="option-label" style="top:527px">OPT.2</p>
  <section class="banner" style="top:440px">
    <svg class="banner__photo" width="618" height="353" role="img" aria-label="Foto eines silbernen Sportwagens auf einer Straße mit Palmen">
      <defs>
        <linearGradient id="carTone" x1="0" y1="0" x2="0" y2="1">
          <stop offset="0" stop-color="#8fb0b3"/>
          <stop offset="0.35" stop-color="#3f5a55"/>
          <stop offset="0.6" stop-color="#c4d4d6"/>
          <stop offset="1" stop-color="#5a5c5e"/>
        </linearGradient>
      </defs>
      <polygon points="422,0 618,0 618,353 321,353" fill="url(#carTone)"/>
    </svg>
    <svg class="banner__band" width="618" height="353" aria-hidden="true">
      <defs>
        <linearGradient id="goldBand2" x1="0" y1="0" x2="1" y2="0">
          <stop offset="0" stop-color="var(--gold-1)"/>
          <stop offset="0.45" stop-color="var(--gold-2)"/>
          <stop offset="1" stop-color="var(--gold-3)"/>
        </linearGradient>
      </defs>
      <polygon points="0,111 404,111 367,226 0,226" fill="url(#goldBand2)"/>
    </svg>
    <p class="brand">NEDRAV</p>
    <p class="price">299€</p>
    <p class="price__lead">CHIPTUNING AB</p>
    <p class="tagline">MEHR LEISTUNG,<br>WENIGER VERBRAUCH</p>
    <ul class="services services--left">
      <li>· CHIPTUNING</li>
      <li>· ECO-OPTIMIERUNG</li>
      <li>· AGR / DPF DEAKTIVIERUNG</li>
    </ul>
    <ul class="services services--right">
      <li>· ZÖL GUTACHTEN</li>
      <li>· SOFTWAREENTWICKLUNG</li>
      <li>· CODIERSERVICE</li>
    </ul>
    <p class="contact">www.nedrav.de | Tel: 01639840517</p>
  </section>

</div>
</body>
</html>
```